Re-brand our business and design!

We need a simple informational website (editable for in the future use)
We need our logo(we have included logo), name, who we are, and what we do displayed.

This is our current site (which is not acceptable, and only a template site): all our information is on this site, please use it forreferanceofinformation.
Www.brightlanefixers.com

Target Market(s)

Real estate brokers, and realtors,homeowners, and anyone looking for home repairs.

Industry/Entity Type

Business

Number of Pages Required

4 page

Font styles to use
Sans Serif

Requirements
Must have
• Our name, contact info, services, and our logo (which we will Email upon request)
• MUST have originality to the site.
• custom "contact us form" or request an estimate form.
Nice to have
• page for real customer testimonies.
• page for our previous work where we can upload pics of completed jobs.
Should not have
• any infringements on any copyrights or plagiarism at all.

```html
<!DOCTYPE html>
<html lang="en">
<head>
<meta charset="utf-8">
<title>Bright Lane Fixers – Home Repairs and Maintenance</title>
<link rel="stylesheet" href="https://fonts.googleapis.com/css2?family=Montserrat:wght@300;400;500;600;700;800&family=Arimo:wght@400&display=swap">
<style>
:root{
  --red:#e30613;
  --red-dark:#c40510;
  --ink:#111111;
  --grey-text:#555555;
  --light:#f3f3f3;
  --white:#ffffff;
}
*{margin:0;padding:0;box-sizing:border-box}
html,body{width:1200px;height:2230px;overflow:hidden;background:var(--white)}
body{position:relative;font-family:"Montserrat",sans-serif;color:var(--ink)}
.abs{position:absolute}

/* header */
.site-header{position:absolute;left:0;top:0;width:1200px;height:125px;background:var(--white);box-shadow:0 2px 6px rgba(0,0,0,.12);z-index:2}
.brand{position:absolute;left:77px;top:34px;width:250px;text-align:center}
.brand-name{font-weight:700;font-size:22px;color:var(--ink);line-height:1.1}
.brand-sub{font-weight:600;font-size:14px;color:#444;margin-top:2px}
.brand-mark{display:inline-block;width:12px;height:12px;background:var(--red);margin-right:8px;vertical-align:middle}
.main-nav a{position:absolute;top:50px;font-size:17px;font-weight:500;color:var(--red);text-decoration:none}
.main-nav a.current{color:var(--ink)}
.call-box{position:absolute;left:862px;top:25px;width:261px;height:73px;border:1px solid #d6d6d6;border-radius:4px;background:linear-gradient(#fafafa,#ececec)}
.call-box svg{position:absolute;left:20px;top:18px}
.call-label{position:absolute;left:74px;top:15px;font-size:13px;color:#444}
.call-number{position:absolute;left:74px;top:31px;font-size:27px;font-weight:500;color:var(--red)}

/* hero */
.hero{position:absolute;left:0;top:125px;width:1200px;height:552px;background:var(--light)}
.hero-photo{position:absolute;left:0;top:0;width:700px;height:552px;background:linear-gradient(90deg,#c7b9a4 0%,#9fb0c0 45%,#d9dde0 80%,rgba(243,243,243,0) 100%)}
.hero-kicker{position:absolute;left:656px;top:140px;font-size:30px;color:var(--red);font-weight:400}
.hero-title{position:absolute;left:654px;top:176px;font-size:62px;font-weight:800;letter-spacing:.5px}
.hero-bar{position:absolute;left:654px;top:247px;width:469px;height:61px;background:var(--red);color:var(--white);font-size:30px;font-weight:300;padding:12px 0 0 23px;letter-spacing:.5px}
.btn-book{position:absolute;left:654px;top:340px;width:250px;height:64px;background:var(--red);color:var(--white);font-size:27px;font-weight:500;text-align:center;line-height:64px;border-radius:3px;box-shadow:0 3px 0 var(--red-dark)}

/* services */
.section-title{position:absolute;left:0;width:1200px;text-align:center;font-size:44px;font-weight:300;letter-spacing:1px}
.section-title strong{color:var(--red);font-weight:700}
.service{position:absolute;top:800px;width:250px;text-align:center}
.service-photo{width:148px;height:148px;border-radius:50%;margin:0 auto;border:2px solid var(--red)}
.service-photo.dark{border-color:var(--ink)}
.service h3{margin-top:30px;font-size:21px;font-weight:500;letter-spacing:.3px}
.service h3.accent{color:var(--red)}
.service p{margin-top:12px;font-family:"Arimo",sans-serif;font-size:14.5px;line-height:23px;color:var(--grey-text)}

/* listing band */
.listing-band{position:absolute;left:0;top:1178px;width:1200px;height:416px;background:#f1eeea;overflow:hidden}
.band-photo-left{position:absolute;left:0;top:0;width:312px;height:416px;background:linear-gradient(135deg,#e9e4dd,#c98f88 55%,#8a6e62)}
.band-photo-right{position:absolute;left:640px;top:0;width:560px;height:416px;background:linear-gradient(160deg,#f3f1ee 0%,#6b80b3 30%,#e6d3b7 60%,#cfae84 100%)}
.band-text{position:absolute;left:308px;top:72px;width:700px}
.band-text h2{font-size:42px;font-weight:500;line-height:52px}
.band-text p{margin-top:16px;font-size:28px;font-weight:500;line-height:36px;color:#333}
.band-phone{margin-top:14px;font-size:42px;font-weight:800;color:var(--red)}

/* testimonials */
.client{position:absolute;top:1729px;width:500px}
.client-photo{width:62px;height:62px;background:linear-gradient(#d7d2cc,#8c7f75)}
.client-name{position:absolute;left:84px;top:20px;font-size:21px;font-weight:500;letter-spacing:.3px}
.client p{margin-top:24px;font-family:"Arimo",sans-serif;font-size:15.5px;line-height:25px;color:var(--grey-text)}

/* footer */
.site-footer{position:absolute;left:0;top:1939px;width:1200px;height:239px;background:var(--red);color:var(--white)}
.footer-col h4{position:absolute;top:30px;font-size:18px;font-weight:500;letter-spacing:.3px}
.contact-line{position:absolute;left:80px;font-family:"Arimo",sans-serif;font-size:14.5px;line-height:21px}
.contact-line svg{position:absolute;left:0;top:2px}
.contact-line span{display:block;margin-left:32px}
.news-item{position:absolute;left:345px;width:230px}
.news-thumb{position:absolute;left:0;top:0;width:52px;height:52px;border-radius:50%;border:2px solid var(--white);background:linear-gradient(#c8b9a3,#6f6250)}
.news-text{margin-left:62px;font-family:"Arimo",sans-serif;font-size:13.5px;line-height:20px}
.news-date{font-size:12px;opacity:.9}
.newsletter-copy{position:absolute;left:610px;top:72px;width:250px;font-family:"Arimo",sans-serif;font-size:13.5px;line-height:24px}
.newsletter-form{position:absolute;left:608px;top:130px;width:250px;height:52px;background:var(--white);border-radius:26px}
.newsletter-form span{position:absolute;left:26px;top:16px;font-family:"Arimo",sans-serif;font-style:italic;font-size:13px;color:#888}
.newsletter-submit{position:absolute;right:0;top:0;width:52px;height:52px;border-radius:50%;background:var(--ink)}
.newsletter-submit svg{position:absolute;left:20px;top:18px}
.footer-brand{position:absolute;left:890px;top:76px;width:230px;text-align:center;font-size:22px;font-weight:700}
.social{position:absolute;top:144px;width:16px;height:16px;border-radius:50%;border:2px solid var(--white)}
.copyright{position:absolute;left:0;top:2178px;width:1200px;height:52px;background:var(--red-dark);color:var(--ink);text-align:center;line-height:52px;font-family:"Arimo",sans-serif;font-size:14px}
</style>
</head>
<body>

<header class="site-header">
  <div class="brand">
    <div class="brand-name"><span class="brand-mark"></span>Bright Lane Fixers</div>
    <div class="brand-sub">And Maintenance</div>
  </div>
  <nav class="main-nav">
    <a class="current" href="#" style="left:391px">Home</a>
    <a href="#" style="left:501px">About</a>
    <a href="#" style="left:613px">Services</a>
    <a href="#" style="left:741px">Contact</a>
  </nav>
  <div class="call-box">
    <svg width="38" height="38" viewBox="0 0 24 24" fill="none" stroke="#222" stroke-width="1.4"><path d="M22 16.9v3a2 2 0 0 1-2.2 2 19.8 19.8 0 0 1-8.6-3.1 19.5 19.5 0 0 1-6-6A19.8 19.8 0 0 1 2.1 4.2 2 2 0 0 1 4.1 2h3a2 2 0 0 1 2 1.7c.1.9.4 1.8.7 2.7a2 2 0 0 1-.5 2.1L8 9.8a16 16 0 0 0 6 6l1.3-1.3a2 2 0 0 1 2.1-.4c.9.3 1.8.6 2.7.7a2 2 0 0 1 1.7 2z"/></svg>
    <div class="call-label">24/7 CALL US ON</div>
    <div class="call-number">555.014.2273</div>
  </div>
</header>

<section class="hero">
  <div class="hero-photo" role="img" aria-label="Couple with house plans looking up at their porch roof"></div>
  <div class="hero-kicker">We see Our Job</div>
  <h1 class="hero-title">AS HELPING</h1>
  <div class="hero-bar">REPAIR YOUR PROPERTY.</div>
  <a class="btn-book">BOOK NOW !</a>
</section>

<h2 class="section-title" style="top:722px">WHAT WE <strong>DO</strong></h2>

<div class="service" style="left:82px">
  <div class="service-photo dark" role="img" aria-label="Carpenter working on a wooden deck" style="background:linear-gradient(#9cc37a,#d49a3a)"></div>
  <h3 class="accent">CARPENTRY</h3>
  <p>Stairs, Floors, Decks, Fences Storage sheds, Storage shelving and doors, Vapor barrier repair/installation, Attic and crawl space</p>
</div>
<div class="service" style="left:346px">
  <div class="service-photo" role="img" aria-label="Plumber fixing pipes under a sink" style="background:linear-gradient(#e6e3df,#9c8a78)"></div>
  <h3>PLUMBING</h3>
  <p>Bathrooms, Kitchens, Washer/Dryer Hook Up, Clogged drains, Toilets, Tubs/Showers, Sinks, Garbage disposals, Leaking faucets, Vent repair</p>
</div>
<div class="service" style="left:610px">
  <div class="service-photo" role="img" aria-label="Worker installing a window frame" style="background:linear-gradient(#5a4a44,#d8d4cf)"></div>
  <h3>DOORS &amp; WINDOWS</h3>
  <p>Weatherstripping, Replacements Glass and Screen Installation and Repair, Install locksets</p>
</div>
<div class="service" style="left:874px">
  <div class="service-photo" role="img" aria-label="Electrician working on a ceiling light fixture" style="background:linear-gradient(#f2f2f2,#5c7bb0)"></div>
  <h3>ELECTRICAL</h3>
  <p>Code/Service Upgrades<br>Fuses and Circuit Breakers<br>Recessed Lighting<br>Ceiling Fixtures</p>
</div>

<section class="listing-band">
  <div class="band-photo-left" role="img" aria-label="Couple browsing home listings on a laptop"></div>
  <div class="band-photo-right" role="img" aria-label="Worker measuring wooden floor boards"></div>
  <div class="band-text">
    <h2>Looking for someone to help get your listing ready to show?</h2>
    <p>A complete Home Repair Solution? Did an inspection reveal repairs needed before closing? Bright Lane Fixers can help!</p>
    <div class="band-phone">555.014.2273</div>
  </div>
</section>

<h2 class="section-title" style="top:1640px">HAPPY <strong>CLIENTS</strong></h2>

<div class="client" style="left:79px">
  <div class="client-photo" role="img" aria-label="Client portrait"></div>
  <div class="client-name">JOHN DOE</div>
  <p>Lorem Ipsum is simply dummy text of the printing and typesetting industry. Lorem Ipsum has been the industry's standard dummy text ever since the 1500s, when an unknown printer took a galley</p>
</div>
<div class="client" style="left:624px">
  <div class="client-photo" role="img" aria-label="Client portrait"></div>
  <div class="client-name">LENA HARWICK</div>
  <p>Lorem Ipsum is simply dummy text of the printing and typesetting industry. Lorem Ipsum has been the industry's standard dummy text ever since the 1500s, when an unknown printer took a galley</p>
</div>

<footer class="site-footer">
  <div class="footer-col"><h4 style="left:80px">CONTACT INFO</h4></div>
  <div class="contact-line" style="top:76px">
    <svg width="20" height="18" viewBox="0 0 24 24" fill="none" stroke="#fff" stroke-width="1.8"><path d="M1 6v16l7-4 8 4 7-4V2l-7 4-8-4-7 4zM8 2v16M16 6v16"/></svg>
    <span>123 Building Name, Strret, Area,<br>Citry, Country - Zipcode</span>
  </div>
  <div class="contact-line" style="top:132px">
    <svg width="18" height="18" viewBox="0 0 24 24" fill="none" stroke="#fff" stroke-width="1.8"><path d="M22 16.9v3a2 2 0 0 1-2.2 2 19.8 19.8 0 0 1-8.6-3.1 19.5 19.5 0 0 1-6-6A19.8 19.8 0 0 1 2.1 4.2 2 2 0 0 1 4.1 2h3a2 2 0 0 1 2 1.7c.1.9.4 1.8.7 2.7a2 2 0 0 1-.5 2.1L8 9.8a16 16 0 0 0 6 6l1.3-1.3a2 2 0 0 1 2.1-.4c.9.3 1.8.6 2.7.7a2 2 0 0 1 1.7 2z"/></svg>
    <span>555.014.2273</span>
  </div>
  <div class="contact-line" style="top:164px">
    <svg width="18" height="18" viewBox="0 0 24 24" fill="none" stroke="#fff" stroke-width="1.8"><path d="M6 9V2h12v7M6 18H4a2 2 0 0 1-2-2v-5a2 2 0 0 1 2-2h16a2 2 0 0 1 2 2v5a2 2 0 0 1-2 2h-2M6 14h12v8H6z"/></svg>
    <span>555.014.2273</span>
  </div>
  <div class="contact-line" style="top:196px">
    <svg width="18" height="16" viewBox="0 0 24 24" fill="none" stroke="#fff" stroke-width="1.8"><path d="M2 4h20v16H2zM2 4l10 9 10-9"/></svg>
    <span>john@brightlanefixers.com</span>
  </div>

  <div class="footer-col"><h4 style="left:345px">NEWS</h4></div>
  <div class="news-item" style="top:72px">
    <div class="news-thumb" role="img" aria-label="News photo"></div>
    <div class="news-text">Lorem Ipsum is simply dummy text of the printing<br><span class="news-date">Today 5:60 pm - 12.06.2016</span></div>
  </div>
  <div class="news-item" style="top:144px">
    <div class="news-thumb" role="img" aria-label="News photo"></div>
    <div class="news-text">Lorem Ipsum is simply dummy text of the printing<br><span class="news-date">Today 2:10 pm - 12.06.2016</span></div>
  </div>

  <div class="footer-col"><h4 style="left:610px">NEWSLETTER</h4></div>
  <div class="newsletter-copy">Subscribe to get news &amp; Updates of our work</div>
  <div class="newsletter-form">
    <span>E-Mail</span>
    <div class="newsletter-submit"><svg width="12" height="16" viewBox="0 0 12 16" fill="none" stroke="#fff" stroke-width="2"><path d="M3 2l6 6-6 6"/></svg></div>
  </div>

  <div class="footer-brand">Bright Lane Fixers</div>
  <span class="social" style="left:925px"></span>
  <span class="social" style="left:967px"></span>
  <span class="social" style="left:1009px"></span>
  <span class="social" style="left:1051px"></span>
</footer>
<div class="copyright">© Bright Lane Fixers - 2016. All Rights Reserved.</div>

</body>
</html>
```